Supplement Rebranding Bottle Design

READ WORD DOCUMENT ATTACHED.
We want to rebrand our current health supplements (see below). We do want it to be modern, vibrant and appealing. Very upscale and elegant as it targets primarily women.
Bottle size: see pictures for bottle size, along with sample bottles that we like; we’re open to any bottle similar to the ones attached.
Current bottles: So ideally, we’d keep the core color on each bottle with a new branding/bottle design. But we're open to your suggestion.

Target Market(s)

mostly women but shouldn't be overly feminine

Requirements
Must have
• see bottle sizes attached

```html
<!DOCTYPE html>
<html lang="en">
<head>
<meta charset="utf-8">
<title>Vital Supplement Label Range</title>
<link href="https://fonts.googleapis.com/css2?family=Montserrat:wght@600;700;800&display=swap" rel="stylesheet">
<style>
:root{
  --backdrop:#d4d4d2;
  --ink:#222222;
  --liver-deep:#6a2546; --liver-accent:#c05590;
  --blood-deep:#41356b; --blood-accent:#6a85c8;
  --hormone-deep:#244c44; --hormone-accent:#88cbad;
  --tummy-deep:#c4262f; --tummy-accent:#f07480;
  --silver:linear-gradient(90deg,#e6e6e6 0%,#ffffff 35%,#f4f4f4 60%,#ffffff 80%,#e2e2e2 100%);
}
*{margin:0;padding:0;box-sizing:border-box}
html,body{width:1200px;height:869px;overflow:hidden}
body{background:var(--backdrop);font-family:'Montserrat',Arial,sans-serif;position:relative;color:var(--ink)}
.label{position:absolute;width:255px;height:277px;background:var(--silver);box-shadow:0 2px 4px rgba(0,0,0,.25);overflow:hidden;text-align:center}
.liver{--deep:var(--liver-deep);--accent:var(--liver-accent)}
.blood{--deep:var(--blood-deep);--accent:var(--blood-accent)}
.hormone{--deep:var(--hormone-deep);--accent:var(--hormone-accent)}
.tummy{--deep:var(--tummy-deep);--accent:var(--tummy-accent)}

/* Classic label */
.classic .top-stripe{height:8px;background:var(--accent)}
.classic .product-name{position:absolute;left:0;right:0;top:32px;height:80px;display:flex;flex-direction:column;justify-content:center;color:var(--deep);font-weight:700;font-size:22px;letter-spacing:.5px;line-height:1.05}
.product-name .prefix{font-size:13px;color:var(--accent);letter-spacing:.5px}
.product-name .ring{display:inline-block;width:10px;height:10px;border:1.5px solid currentColor;border-radius:50%;margin-left:6px;vertical-align:middle;opacity:.7}
.classic .benefit-band{position:absolute;left:0;right:0;top:121px;height:98px;background:var(--deep);color:#fff;font-weight:700;font-size:14px;letter-spacing:.6px;line-height:18px;padding-top:27px}
.classic .pill{position:absolute;left:20px;width:216px;top:205px;height:28px;border-radius:14px;background:var(--accent);color:#fff;font-weight:700;font-size:13px;letter-spacing:.6px;line-height:28px}
.classic .footer{position:absolute;left:10px;right:10px;bottom:6px;display:flex;justify-content:space-between;font-size:8.5px;font-weight:700;letter-spacing:.3px;color:var(--ink)}
.footer .qty{color:var(--accent)}
.footer .qty b{color:var(--ink)}

/* Arched label */
.arched{height:275px}
.arched .arch{position:absolute;left:0;top:0;width:255px;height:116px}
.arched .product-name{position:absolute;left:0;right:0;top:22px;height:70px;display:flex;flex-direction:column;justify-content:center;color:#fff;font-weight:700;font-size:20px;letter-spacing:.8px;line-height:1.1}
.arched .benefit{position:absolute;left:0;right:0;top:139px;font-weight:700;font-size:13.5px;letter-spacing:.6px;line-height:18px;color:var(--ink)}
.arched .divider{position:absolute;left:110px;width:34px;top:194px;height:2px;background:var(--accent)}
.arched .kind{position:absolute;left:0;right:0;top:210px;font-weight:700;font-size:13.5px;letter-spacing:.6px}
.arched .footer-bar{position:absolute;left:0;right:0;bottom:0;height:24px;background:var(--deep);display:flex;justify-content:space-between;align-items:center;padding:0 10px;font-size:8.5px;font-weight:700;letter-spacing:.3px;color:#fff}
.footer-bar .qty{color:var(--accent)}
.footer-bar .qty b{color:#fff}
</style>
</head>
<body>

<!-- Classic range -->
<section class="label classic liver" style="left:60px;top:157px">
  <div class="top-stripe"></div>
  <h2 class="product-name"><span>LIVER VITAL<span class="ring"></span></span></h2>
  <p class="benefit-band">REJUVENATING CLEANSE<br>&amp; DETOX FORMULA*</p>
  <p class="pill">DIETARY SUPPLEMENT</p>
  <p class="footer"><span class="qty">QTY <b>120</b></span><span>VEGETABLE CAPSULES</span></p>
</section>
<section class="label classic blood" style="left:337px;top:157px">
  <div class="top-stripe"></div>
  <h2 class="product-name"><span class="prefix">BLOOD</span><span>SUGER VITAL<span class="ring"></span></span></h2>
  <p class="benefit-band">REJUVENATING CLEANSE<br>&amp; DETOX FORMULA*</p>
  <p class="pill">DIETARY SUPPLEMENT</p>
  <p class="footer"><span class="qty">QTY <b>120</b></span><span>VEGETABLE CAPSULES</span></p>
</section>
<section class="label classic hormone" style="left:615px;top:157px">
  <div class="top-stripe"></div>
  <h2 class="product-name"><span>HORMONE VITAL<span class="ring"></span></span></h2>
  <p class="benefit-band">REJUVENATING CLEANSE<br>&amp; DETOX FORMULA*</p>
  <p class="pill">DIETARY SUPPLEMENT</p>
  <p class="footer"><span class="qty">QTY <b>120</b></span><span>VEGETABLE CAPSULES</span></p>
</section>
<section class="label classic tummy" style="left:886px;top:157px">
  <div class="top-stripe"></div>
  <h2 class="product-name"><span>TUMMY VITAL<span class="ring"></span></span></h2>
  <p class="benefit-band">REJUVENATING CLEANSE<br>&amp; DETOX FORMULA*</p>
  <p class="pill">DIETARY SUPPLEMENT</p>
  <p class="footer"><span class="qty">QTY <b>120</b></span><span>VEGETABLE CAPSULES</span></p>
</section>

<!-- Arched range -->
<section class="label arched liver" style="left:59px;top:478px">
  <svg class="arch" viewBox="0 0 255 116" aria-hidden="true"><path d="M0 0H255V92Q127.5 130 0 92Z" fill="var(--deep)"/></svg>
  <h2 class="product-name"><span>LIVER VITAL<span class="ring"></span></span></h2>
  <p class="benefit">REJUVENATING CLEANSE<br>&amp; DETOX FORMULA*</p>
  <div class="divider"></div>
  <p class="kind">DIETARY SUPPLEMENT</p>
  <p class="footer-bar"><span class="qty">QTY <b>120</b></span><span>VEGETABLE CAPSULES</span></p>
</section>
<section class="label arched blood" style="left:334px;top:478px">
  <svg class="arch" viewBox="0 0 255 116" aria-hidden="true"><path d="M0 0H255V92Q127.5 130 0 92Z" fill="var(--deep)"/></svg>
  <h2 class="product-name"><span class="prefix">BLOOD</span><span>SUGER VITAL<span class="ring"></span></span></h2>
  <p class="benefit">SUPPORTS HEALTHY<br>BLOOD GLUCOSE LEVELS*</p>
  <div class="divider"></div>
  <p class="kind">DIETARY SUPPLEMENT</p>
  <p class="footer-bar"><span class="qty">QTY <b>60</b></span><span>VEGETABLE CAPSULES</span></p>
</section>
<section class="label arched hormone" style="left:610px;top:478px">
  <svg class="arch" viewBox="0 0 255 116" aria-hidden="true"><path d="M0 0H255V92Q127.5 130 0 92Z" fill="var(--deep)"/></svg>
  <h2 class="product-name" style="top:14px"><span>HORMONE VITAL<span class="ring"></span></span></h2>
  <p class="benefit" style="font-size:14.5px">SUPPORTS HEALTHY<br>HORMONE LEVELS*</p>
  <div class="divider"></div>
  <p class="kind">DIETARY SUPPLEMENT</p>
  <p class="footer-bar"><span class="qty">QTY <b>60</b></span><span>VEGETABLE CAPSULES</span></p>
</section>
<section class="label arched tummy" style="left:887px;top:478px">
  <svg class="arch" viewBox="0 0 255 116" aria-hidden="true"><path d="M0 0H255V92Q127.5 130 0 92Z" fill="var(--deep)"/></svg>
  <h2 class="product-name" style="top:14px"><span>TUMMY VITAL<span class="ring"></span></span></h2>
  <p class="benefit" style="font-size:14.5px">SUPPORTS HEALTHY<br>HORMONE LEVELS*</p>
  <div class="divider"></div>
  <p class="kind">DIETARY SUPPLEMENT</p>
  <p class="footer-bar"><span class="qty">QTY <b>60</b></span><span>VEGETABLE CAPSULES</span></p>
</section>

</body>
</html>
```